Business Card Design Project

We are not a new company, but renamed to "Norvane Kitchens" last year. We specialize in modern high-end cabinetry imports. We would like to communicate a sense of quality and cutting edge technology. Ideally the design would incorporate our logo colors, silver, red and preferably a black, matte background. Though we are open to suggestions.
Logo is attached.
Edit: I have attached rough drafts of the previous cards, this way you will have all necessary content that needs to go on the cards.
Updates
Project Deadline Extended
Reason: We have received a lot of great designs, but due to the sheer number we couldn't respond to all. We will extend the deadline for another 7 days to finalize and provide feedback to designers.
Thank you for your hard work!
Industry/Entity Type
Business
Look and feel
Each slider illustrates characteristics of the customer's brand and the style your logo design should communicate.

```html
<!DOCTYPE html>
<html lang="en">
<head>
<meta charset="utf-8">
<title>Norvane Kitchens Business Card</title>
<link href="https://fonts.googleapis.com/css2?family=Michroma&display=swap" rel="stylesheet">
<style>
  :root {
    --page: #d8d8d8;
    --card-black: #0b0b0b;
    --card-panel: #1a1a1a;
    --card-edge: #3a3a3a;
    --accent-red: #e0201c;
    --silver: #d6d6d6;
    --text-white: #f2f2f2;
  }
  * { margin: 0; padding: 0; box-sizing: border-box; }
  html, body {
    width: 1200px; height: 861px; overflow: hidden;
    background: var(--page);
    font-family: "Michroma", "Arial", sans-serif;
  }
  .sheet {
    width: 1200px; height: 861px;
    display: flex; align-items: center; justify-content: center; gap: 36px;
  }
  .card {
    position: relative;
    width: 560px; height: 320px;
    background: radial-gradient(ellipse at 55% 40%, #222 0%, var(--card-black) 75%);
    border: 1px solid var(--card-edge);
    box-shadow: 0 10px 24px rgba(0,0,0,.35);
    overflow: hidden;
  }
  /* back side */
  .card-back .info-panel {
    position: absolute; top: 0; right: 0; bottom: 0; width: 58%;
    background: linear-gradient(135deg, #262626 0%, var(--card-panel) 60%, #121212 100%);
    clip-path: polygon(8% 0, 100% 0, 100% 100%, 0 100%);
  }
  .identity {
    position: absolute; left: 0; width: 46%; top: 176px;
    text-align: right; padding-right: 8px;
  }
  .identity-name {
    color: var(--accent-red); font-size: 15px; letter-spacing: .5px;
    text-transform: uppercase;
  }
  .identity-title {
    color: var(--text-white); font-size: 10px; margin-top: 4px;
  }
  .contact-list {
    position: absolute; left: 49%; top: 62px;
    list-style: none;
  }
  .contact-item {
    display: flex; align-items: flex-start; gap: 12px;
    color: var(--text-white); font-size: 9px; letter-spacing: .8px;
    text-transform: uppercase; line-height: 1.5; margin-bottom: 11px;
  }
  .contact-item .icon { flex: 0 0 16px; width: 16px; height: 16px; }
  /* front side */
  .card-front { display: flex; align-items: center; justify-content: center; }
  .brand {
    display: flex; align-items: center; gap: 14px;
    color: var(--silver); font-size: 22px; letter-spacing: 1.5px;
    text-transform: uppercase;
  }
  .brand-mark {
    width: 18px; height: 18px; background: var(--accent-red);
  }
</style>
</head>
<body>
<main class="sheet">
  <section class="card card-back" aria-label="Card back with contact details">
    <div class="info-panel"></div>
    <div class="identity">
      <p class="identity-name">Marcus Delane</p>
      <p class="identity-title">President</p>
    </div>
    <ul class="contact-list">
      <li class="contact-item">
        <svg class="icon" viewBox="0 0 16 16" aria-hidden="true"><circle cx="8" cy="8" r="8" fill="var(--accent-red)"/><path d="M8 3.5a2.6 2.6 0 0 0-2.6 2.6C5.4 8.2 8 11.5 8 11.5s2.6-3.3 2.6-5.4A2.6 2.6 0 0 0 8 3.5z" fill="#fff"/><circle cx="8" cy="6.1" r="1" fill="var(--accent-red)"/></svg>
        <span>2158 - 84 St.<br>Calder, AB T5K 3M2</span>
      </li>
      <li class="contact-item">
        <svg class="icon" viewBox="0 0 16 16" aria-hidden="true"><circle cx="8" cy="8" r="8" fill="var(--accent-red)"/><path d="M5 4.2l1.6-.2.8 2-1 .8a6 6 0 0 0 2.8 2.8l.8-1 2 .8-.2 1.6c-3.8.2-7-3-6.8-6.8z" fill="#fff"/></svg>
        <span>555.210.0187</span>
      </li>
      <li class="contact-item">
        <svg class="icon" viewBox="0 0 16 16" aria-hidden="true"><circle cx="8" cy="8" r="8" fill="var(--accent-red)"/><rect x="4.5" y="6.5" width="7" height="4.5" fill="#fff"/><rect x="5.8" y="4.3" width="4.4" height="2.2" fill="#fff"/></svg>
        <span>555.210.0192</span>
      </li>
      <li class="contact-item">
        <svg class="icon" viewBox="0 0 16 16" aria-hidden="true"><circle cx="8" cy="8" r="8" fill="var(--accent-red)"/><rect x="5.8" y="3.6" width="4.4" height="8.8" rx=".8" fill="#fff"/><rect x="6.6" y="4.8" width="2.8" height="5" fill="var(--accent-red)"/></svg>
        <span>555.318.40276</span>
      </li>
      <li class="contact-item">
        <svg class="icon" viewBox="0 0 16 16" aria-hidden="true"><circle cx="8" cy="8" r="8" fill="var(--accent-red)"/><rect x="4.2" y="5.2" width="7.6" height="5.6" fill="#fff"/><path d="M4.2 5.2L8 8.4l3.8-3.2" fill="none" stroke="var(--accent-red)" stroke-width=".9"/></svg>
        <span>marcus@norvanekitchens.ca</span>
      </li>
      <li class="contact-item">
        <svg class="icon" viewBox="0 0 16 16" aria-hidden="true"><circle cx="8" cy="8" r="8" fill="var(--accent-red)"/><circle cx="8" cy="8" r="3.8" fill="none" stroke="#fff" stroke-width=".9"/><path d="M4.2 8h7.6M8 4.2c-1.6 2.2-1.6 5.4 0 7.6M8 4.2c1.6 2.2 1.6 5.4 0 7.6" fill="none" stroke="#fff" stroke-width=".8"/></svg>
        <span>www.norvanekitchens.ca</span>
      </li>
    </ul>
  </section>

  <section class="card card-front" aria-label="Card front with company name">
    <div class="brand">
      <span class="brand-mark" aria-hidden="true"></span>
      <span class="brand-name">Norvane Kitchens</span>
    </div>
  </section>
</main>
</body>
</html>
```